Packaging Design Project

I need a box for a hair oil called NEL. 3 color, Simple design .. We are open to new ideas, the over all theme.. Pure and Simple , Natural, Color protect, good for the hair. We started with a basic design and this is the existing website http://nelhaircare.com/

Industry/Entity Type

Hair

```html
<!DOCTYPE html>
<html lang="en">
<head>
<meta charset="utf-8">
<title>NEL Hair Care – Hair Oil Box</title>
<link rel="stylesheet" href="https://fonts.googleapis.com/css2?family=Arimo:wght@400;700&family=Roboto+Condensed:wght@700&display=swap">
<style>
:root{
  --blue-light:#2a74b8;
  --blue-mid:#1a5aa0;
  --blue-deep:#0c3b78;
  --accent:#3a9ae6;
  --dark:#2b2826;
  --ink:#111;
  --paper:#fff;
  --rule:#b9b9b9;
  --hair-a:#7a3e24;
  --hair-b:#3d1b10;
}
*{margin:0;padding:0;box-sizing:border-box}
html,body{width:1022px;height:1200px;overflow:hidden;background:var(--paper)}
body{position:relative;font-family:"Arimo",Arial,sans-serif;color:var(--ink)}
.abs{position:absolute}

/* structure */
.strip{left:0;top:192px;width:1022px;height:815px;border:1px solid var(--rule)}
.band-dark{background:var(--dark)}
.band-white{background:var(--paper)}
.band-blue{background:linear-gradient(180deg,var(--blue-mid),var(--blue-light) 40%,var(--blue-deep))}
.dash{height:0;border-top:3px dashed var(--accent)}
.fold{width:1px;background:var(--rule)}

/* brand name */
.brand{color:var(--blue-deep);font-weight:700;text-align:center;line-height:1;font-family:"Arimo",Arial,sans-serif}
.brand .name{display:block;font-size:40px;letter-spacing:2px}
.brand .sub{display:block;font-size:17px;margin-top:4px;letter-spacing:1px}
.brand.large .name{font-size:62px}
.brand.large .sub{font-size:26px}

/* copy */
.directions{left:14px;top:432px;width:296px;color:var(--paper);font-size:14.5px;line-height:16.5px;text-align:center}
.directions h2{font-size:14.5px;font-weight:700;margin-bottom:17px}
.directions p{margin-bottom:16px}
.directions b{font-weight:700}

.claims{left:514px;top:462px;width:321px;color:var(--paper);text-align:center}
.claims h1{font-family:"Roboto Condensed","Arial Narrow",sans-serif;font-size:18px;line-height:23px}
.claims p{font-weight:700;font-size:22px;line-height:28.5px;margin-top:32px}

.side-info{left:835px;top:490px;width:187px;color:var(--paper);text-align:center;font-size:16px;line-height:19px}
.side-info p+p{margin-top:26px}

.icons{left:322px;top:420px;width:192px}
.icon{display:flex;flex-direction:column;align-items:center;margin-bottom:26px}
.icon svg{width:46px;height:46px}
.icon span{font-size:7.5px;font-weight:700;color:var(--ink);text-align:center;line-height:9px;margin-top:4px}

.footer{top:932px;height:58px;display:flex;align-items:center;justify-content:center;text-align:center;font-weight:700;font-size:17px}
.footer.web{font-weight:400;font-size:16px;line-height:20px;flex-direction:column}
.footer.web b{font-weight:700}
.footer.badges{font-size:15px;line-height:18px}

.portrait{background:linear-gradient(160deg,#d8b29c 0%,var(--hair-a) 35%,var(--hair-b) 100%);border-radius:48% 40% 0 0/30% 25% 0 0}
</style>
</head>
<body>

<!-- top flap (upside down) -->
<div class="abs band-blue" style="left:514px;top:0;width:321px;height:40px"></div>
<div class="abs dash" style="left:514px;top:40px;width:321px"></div>
<div class="abs band-white" style="left:514px;top:45px;width:321px;height:92px"></div>
<div class="abs brand" style="left:514px;top:58px;width:321px;transform:rotate(180deg)"><span class="name">NEL</span><span class="sub">HAIR CARE</span></div>
<div class="abs band-dark" style="left:514px;top:137px;width:321px;height:56px" role="img" aria-label="dark floral pattern band"></div>
<div class="abs dash" style="left:514px;top:145px;width:321px"></div>
<div class="abs" style="left:514px;top:0;width:321px;height:192px;border:1px solid var(--rule);border-bottom:none"></div>

<!-- main strip -->
<div class="abs band-dark" style="left:0;top:192px;width:1022px;height:78px" role="img" aria-label="dark floral pattern band"></div>
<div class="abs dash" style="left:0;top:271px;width:1022px"></div>
<div class="abs band-white" style="left:0;top:276px;width:1022px;height:90px"></div>
<div class="abs" style="left:0;top:366px;width:1022px;height:6px;background:var(--blue-mid)"></div>
<div class="abs band-blue" style="left:0;top:372px;width:1022px;height:560px" role="img" aria-label="blue floral pattern background"></div>
<div class="abs dash" style="left:0;top:380px;width:1022px;opacity:.7"></div>
<div class="abs band-white" style="left:0;top:932px;width:1022px;height:58px"></div>
<div class="abs" style="left:0;top:990px;width:1022px;height:17px;background:var(--blue-mid)"></div>
<div class="abs strip"></div>
<div class="abs fold" style="left:322px;top:192px;height:815px"></div>
<div class="abs fold" style="left:514px;top:192px;height:815px"></div>
<div class="abs fold" style="left:835px;top:192px;height:815px"></div>

<!-- brand names on panels -->
<div class="abs brand" style="left:0;top:296px;width:322px"><span class="name">NEL</span><span class="sub">HAIR CARE</span></div>
<div class="abs brand" style="left:322px;top:296px;width:192px"><span class="name">NEL</span><span class="sub">HAIR CARE</span></div>
<div class="abs brand large" style="left:514px;top:276px;width:321px"><span class="name">NEL</span><span class="sub">HAIR CARE</span></div>
<div class="abs brand" style="left:835px;top:296px;width:187px"><span class="name">NEL</span><span class="sub">HAIR CARE</span></div>

<!-- left panel -->
<section class="abs directions">
  <h2>DIRECTIONS FOR USE:</h2>
  <p><b>As a styling aid:</b> Rub a small amount of product into hands, to damp hair starting from ends up and style as usual.</p>
  <p><b>As an oil treatment:</b> 1-2 times a week apply liberally to dry hair, leave on for 10 minutes and wash a usual.</p>
  <p>Lorem ipsum dolor sit amet, consectetur adipiscing elit. Cras non venenatis nisl. Nam consequat purus id odio vulputate iaculis. Maecenas congue diam justo. Etiam quis mi in libero rutrum gravida. Etiam pharetra volutpat diam nec porta. Maecenas hendrerit accumsan eros non sollicitudin. Curabitur vitae justo ut quam pellentesque accumsan. Quisque posuere risus ut diam pharetra ut fringilla turpis ultricies. Maecenas a erat sit amet odio rhoncus lacinia. Sed est nibh, placerat ac dictum malesuada,</p>
  <p><b>elementum sit</b> amet erat. Quisque mattis ante sed leo sollicitudin at gravida odio lacinia.</p>
</section>

<!-- icon panel -->
<section class="abs icons">
  <div class="icon"><svg viewBox="0 0 46 46"><circle cx="23" cy="23" r="19" fill="none" stroke="#111" stroke-width="3"/></svg><span>not tested<br>on animals</span></div>
  <div class="icon"><svg viewBox="0 0 46 46"><circle cx="23" cy="23" r="19" fill="#111"/></svg><span>natural</span></div>
  <div class="icon"><svg viewBox="0 0 46 46"><circle cx="23" cy="23" r="19" fill="none" stroke="#111" stroke-width="3"/></svg><span>all hair types</span></div>
  <div class="icon"><svg viewBox="0 0 46 46"><circle cx="23" cy="23" r="17" fill="none" stroke="#111" stroke-width="3"/><line x1="11" y1="11" x2="35" y2="35" stroke="#111" stroke-width="3"/></svg><span>paraben-sulfate free</span></div>
  <div class="icon"><svg viewBox="0 0 46 46"><circle cx="23" cy="23" r="19" fill="#111"/></svg><span>made with<br>recycled materials</span></div>
</section>

<!-- front panel -->
<section class="abs claims">
  <h1>PROTECTIVE HAIR-OIL<br>TREATMENT AND STYLING AID</h1>
  <p>Style, Smooth, Shine<br>&amp; Condition<br>ALL Hair types while<br>locking in Moisture</p>
</section>
<div class="abs portrait" style="left:568px;top:655px;width:250px;height:335px" role="img" aria-label="photo of a woman in profile with long straight auburn hair"></div>

<!-- right panel -->
<section class="abs side-info">
  <p>Formulated for NEL<br>Elmcrest Heights,<br>California</p>
  <p>For more formation<br>visit us online at:<br>www.nelhaircare.com</p>
</section>
<div class="abs portrait" style="left:852px;top:735px;width:170px;height:255px" role="img" aria-label="photo of a woman in profile with long straight auburn hair"></div>

<!-- footer strip -->
<div class="abs footer web" style="left:0;width:322px"><span>visit us online at:</span><b>www.nelhaircare.com</b></div>
<div class="abs footer" style="left:322px;width:192px">Made in USA</div>
<div class="abs footer badges" style="left:514px;width:321px;background:rgba(255,255,255,.85)">PARABEN FREE - SULFATE FREE<br>ALLERGY TESTED - ALCOHOL FREE</div>
<div class="abs footer" style="left:835px;width:187px;background:rgba(255,255,255,.85)">100ml / 3/4 oz</div>

<!-- bottom flap -->
<div class="abs band-dark" style="left:514px;top:1007px;width:321px;height:37px" role="img" aria-label="dark floral pattern band"></div>
<div class="abs dash" style="left:514px;top:1046px;width:321px"></div>
<div class="abs band-white" style="left:514px;top:1051px;width:321px;height:86px"></div>
<div class="abs brand" style="left:514px;top:1068px;width:321px"><span class="name">NEL</span><span class="sub">HAIR CARE</span></div>
<div class="abs band-blue" style="left:514px;top:1137px;width:321px;height:63px" role="img" aria-label="blue floral pattern background"></div>
<div class="abs dash" style="left:514px;top:1143px;width:321px;opacity:.7"></div>
<div class="abs" style="left:514px;top:1007px;width:321px;height:193px;border:1px solid var(--rule);border-top:none"></div>

</body>
</html>
```